Diesel Fitting/Mechanical Company Needs a new Business Card

We would like a new business card that showcases our logo and business information.

Industry/Entity Type

Business

Contact Information for Business Card

314 Wendale Street
PO Box 7581 BRAMLEIGH VALE QLD 4936
Phone: 49312787 Fax: 49312688 Mobile: 0438915276 ABN: 63 519 087 342

Requirements
Must have
• The following email addresses:
• admin@tkservicing.com.au , sales@tkservicing.com.au , accounts@tkservicing.com.au , parts@tkservicing.com.au , office@tkservicing.com.au
• Also need to have the website: www.tkservicing.com.au

```html
<!DOCTYPE html>
<html lang="en">
<head>
<meta charset="utf-8">
<title>TK Servicing – Business Card</title>
<link rel="stylesheet" href="https://fonts.googleapis.com/css2?family=Noto+Serif:wght@400;700&display=swap">
<style>
  :root {
    --brand-blue: #0070b0;
    --card-white: #ffffff;
    --panel-grey: #ececec;
    --panel-grey-light: #f8f8f8;
    --text-grey: #4d4d4d;
    --brand-orange: #ef7a35;
    --page-bg: #ffffff;
  }
  * { box-sizing: border-box; margin: 0; padding: 0; }
  html, body { width: 945px; height: 1200px; overflow: hidden; background: var(--page-bg); }
  body { position: relative; font-family: "Noto Serif", Georgia, serif; color: var(--text-grey); }

  .card-front {
    position: absolute; left: 0; top: 0; width: 945px; height: 566px;
    border: 1px solid #d6d6d6;
  }
  .contact-panel {
    position: absolute; left: 0; top: 0; width: 514px; height: 566px;
    background: var(--card-white);
  }
  .band { position: absolute; left: 0; width: 514px; height: 30px; background: var(--brand-blue); }
  .band-top { top: 0; }
  .band-bottom { bottom: 0; }

  .contact-list { position: absolute; left: 0; top: 81px; list-style: none; }
  .contact-item {
    position: relative; height: 40.4px; padding-left: 102px;
    font-size: 26.5px; line-height: 40.4px; white-space: nowrap; letter-spacing: 0.2px;
  }
  .contact-icon { position: absolute; left: 55px; top: 6px; width: 31px; height: 29px; }

  .brand-panel {
    position: absolute; left: 514px; top: 0; width: 431px; height: 566px;
    background: radial-gradient(ellipse at 55% 30%, var(--panel-grey-light), var(--panel-grey) 80%);
  }
  .brand-divider { position: absolute; left: 0; top: 278px; width: 431px; height: 10px; background: var(--brand-blue); }
  .brand-name {
    position: absolute; left: 0; width: 431px; top: 120px;
    display: flex; align-items: center; justify-content: center; gap: 14px;
    font-weight: 700; font-size: 46px; color: var(--brand-orange);
  }
  .brand-dot { width: 26px; height: 26px; border-radius: 50%; background: var(--brand-orange); }
  .address {
    position: absolute; left: 0; width: 431px; top: 371px;
    text-align: center; font-size: 26.5px; line-height: 40.4px; font-style: normal;
  }

  .card-back {
    position: absolute; left: 0; top: 634px; width: 945px; height: 566px;
    background: var(--brand-blue);
  }
  .back-name {
    position: absolute; left: 0; top: 0; width: 945px; height: 566px;
    display: flex; align-items: center; justify-content: center; gap: 24px;
    font-weight: 700; font-size: 84px; color: var(--card-white);
  }
  .back-name .brand-dot { width: 46px; height: 46px; background: var(--card-white); }
</style>
</head>
<body>
  <section class="card-front">
    <div class="contact-panel">
      <div class="band band-top"></div>
      <ul class="contact-list">
        <li class="contact-item">
          <svg class="contact-icon" viewBox="0 0 31 29"><rect width="31" height="29" rx="6" fill="#0070b0"/><path d="M7 12c0-3 4-5 8.5-5S24 9 24 12h-4v-2h-9v2z" fill="#fff"/><rect x="9" y="13" width="13" height="8" rx="2" fill="#fff"/><circle cx="15.5" cy="17" r="2" fill="#0070b0"/></svg>
          Phone: 49312787
        </li>
        <li class="contact-item">
          <svg class="contact-icon" viewBox="0 0 31 29"><rect width="31" height="29" rx="6" fill="#0070b0"/><rect x="10" y="5" width="11" height="7" fill="#fff"/><rect x="7" y="12" width="17" height="11" rx="1.5" fill="none" stroke="#fff" stroke-width="2"/><rect x="10" y="15" width="11" height="2" fill="#fff"/><rect x="10" y="19" width="11" height="2" fill="#fff"/></svg>
          Fax : 49312688
        </li>
        <li class="contact-item">
          <svg class="contact-icon" viewBox="0 0 31 29"><rect width="31" height="29" rx="6" fill="#0070b0"/><path d="M10 6l4 4-2 3c1 2 3 4 5 5l3-2 4 4-3 3c-7 0-14-7-14-14z" fill="#fff"/></svg>
          Mobile: 0438915276
        </li>
        <li class="contact-item">ABN: 63 519 087 342</li>
        <li class="contact-item">
          <svg class="contact-icon" viewBox="0 0 31 29"><rect width="31" height="29" rx="6" fill="#0070b0"/><rect x="7" y="9" width="17" height="11" fill="none" stroke="#fff" stroke-width="1.6"/><path d="M7 9l8.5 6 8.5-6M7 20l6-5M24 20l-6-5" fill="none" stroke="#fff" stroke-width="1.4"/></svg>
          admin@tkservicing.com.au
        </li>
        <li class="contact-item">sales@tkservicing.com.au</li>
        <li class="contact-item">accounts@tkservicing.com.au</li>
        <li class="contact-item">parts@tkservicing.com.au</li>
        <li class="contact-item">office@tkservicing.com.au</li>
        <li class="contact-item">
          <svg class="contact-icon" viewBox="0 0 31 29"><rect width="31" height="29" rx="6" fill="#0070b0"/><g fill="none" stroke="#fff" stroke-width="1.3"><circle cx="15.5" cy="14.5" r="8"/><ellipse cx="15.5" cy="14.5" rx="3.5" ry="8"/><path d="M7.5 14.5h16M9 10h13M9 19h13"/></g></svg>
          www.tkservicing.com.au
        </li>
      </ul>
      <div class="band band-bottom"></div>
    </div>

    <div class="brand-panel">
      <div class="brand-name"><span class="brand-dot"></span>TK Servicing</div>
      <div class="brand-divider"></div>
      <address class="address">
        314 Wendale Street,<br>
        PO Box 7581,<br>
        BRAMLEIGH VALE<br>
        QLD 4936
      </address>
    </div>
  </section>

  <section class="card-back">
    <div class="back-name"><span class="brand-dot"></span>TK Servicing</div>
  </section>
</body>
</html>
```